Lumaridge Hauling

WHY: So we are looking for a clean blue/modern/ mobile friendly website to be able compete with our rival, which is bellhops.comWHO: Our company is based out Atlanta,GA. The Company named is called "LumaRidge Hauling" and we are Professional staffing Agency that trained our employees for Household Industry related tasks such as Moving Furniture, Packers Household Boxes , Vondra Furniture Installers, Mounting TV and etc.WHAT: Our Main Function is we need to be able to pre-qualified lead/schedule them based on availability /Book our client online on Quenpay in order to help our client solve and their problem faster than the traditional 20 min phone call. We need an :Pre-Survey Form /Basic Contact Form Example Below...Desired Button Placement: Should be In the Center or Right Corner. * Q1. What would you like help with? (multi-Choice A to D?* Q2. What are you packing or unpacking* Q3. How many boxes would you like packed or unpacked?* Q4.In Additional to packing or unpacking, do you need any other service>* Q5. Would you like to add photos of the primary item you need packed on..* Q6. When would you like the packing specialist?* Q7. WHat time work best for your schedule?* Q8.Anything else the packing specialist should know? * Q8. Zip Code * Q9. Name* Q10. Email (Privacy Disclaimer)* Q12. Number * Q13. Customer Credit Card InfoWHEN: we looking to be done submit all of our revision request and the project done before New Year, Jan.1

Target Market(s)

Womans: Between 25yr to +55 Womans, Affluence,

Industry/Entity Type

Moving

Number of Pages Required

2 page

Font styles to use
Sans Serif

Colors

Designer to choose colors to be used in the design.

Requirements
Must have
• Service Option Category
• Packers/Installer/ Rental Trucks Assistant
• How it Work Session
• 1.Pick a Service
• 2.Book A Time
• 3.Secured A Payment
Nice to have
• Our Main Function is we need to be able to pre-qualified lead/schedule them based on availability /Book our client online on Quenpay in order to help our client solve and their problem faster than the traditional 20 min phone call.
• We need an :Pre-Survey Form /Basic Contact Form Example Below...
• Desired Button Placement: Should be In the Center or Right Corner.
• * Q1. What would you like help with? (multi-Choice A to D?
• * Q2. What are you packing or unpacking
• * Q3. How many boxes would you like packed or unpacked?
• * Q4.In Additional to packing or unpacking, do you need any other service>
• * Q5. Would you like to add photos of the primary item you need packed on..
• * Q6. When would you like the packing specialist?
• * Q7. WHat time work best for your schedule?
• * Q8.Anything else the packing specialist should know?
• * Q8. Zip Code
• * Q9. Name
• * Q10. Email (Privacy Disclaimer)
• * Q12. Number
• * Q13. Customer Credit Card Info
Should not have
• we are not interesting for an Basic Template Design /generic Truck photo stock/ traditional moving company website).

```html
<!DOCTYPE html>
<html lang="en">
<head>
<meta charset="utf-8">
<title>LumaRidge Hauling</title>
<link href="https://fonts.googleapis.com/css2?family=Montserrat:wght@400;500;600;700;800&display=swap" rel="stylesheet">
<style>
:root{
  --blue:#0a8fd0;
  --blue-dark:#0677b0;
  --ink:#1b1b1b;
  --text:#555b66;
  --muted:#8a909a;
  --soft:#f4f6fa;
  --line:#dfe3ea;
  --white:#ffffff;
  --black:#0d0d0d;
}
*{margin:0;padding:0;box-sizing:border-box}
html,body{width:1200px;height:3681px;overflow:hidden}
body{font-family:"Montserrat",Arial,sans-serif;color:var(--text);background:var(--white);position:relative}
.abs{position:absolute}
.center{text-align:center}
.topbar{left:0;top:0;width:1200px;height:29px;background:var(--black);color:var(--white);font-size:11px;font-weight:500}
.topbar .call{left:81px;top:8px}
.topbar .call b{color:var(--blue);font-weight:600}
.topbar .promo{left:0;width:1200px;top:8px;text-align:center}
.topbar .promo span{color:var(--blue)}
.topbar .signup{left:932px;top:8px}
.topbar .socials{left:1034px;top:9px;display:flex;gap:8px}
.topbar .socials i{display:block;width:10px;height:10px;background:#cfd3d8;border-radius:2px}
.nav{left:0;top:29px;width:1200px;height:81px;background:var(--white)}
.logo{font-weight:800;color:var(--ink);font-size:30px;letter-spacing:-0.5px}
.nav .logo{left:79px;top:22px}
.nav a{position:absolute;top:35px;font-size:11px;font-weight:600;color:var(--ink);text-decoration:none}
.nav a.active{color:var(--blue)}
.nav a.active::after{content:"";position:absolute;left:0;right:0;top:-37px;height:3px;background:var(--blue)}
.btn{display:inline-block;border-radius:30px;font-weight:600;text-align:center;text-decoration:none}
.btn-solid{background:var(--blue);color:var(--white)}
.btn-line{border:1.5px solid var(--blue);color:var(--blue);background:var(--white)}
.nav .btn{left:991px;top:25px;width:128px;height:34px;line-height:34px;font-size:11px}
.hero{left:0;top:110px;width:1200px;height:437px;background:linear-gradient(100deg,#c9b8a4 0%,#d9ccb9 30%,#b89c7c 55%,#e7e2da 80%,#dcd6cf 100%)}
.hero h1{left:81px;top:152px;font-size:33px;font-weight:700;color:var(--ink);line-height:36px}
.hero h1 span{color:var(--blue)}
.hero .btn{left:81px;top:255px;width:120px;height:32px;line-height:29px;font-size:11px}
.quote-accent{left:988px;top:110px;width:121px;height:40px;background:var(--blue)}
.quote{left:827px;top:196px;width:282px;height:386px;background:var(--white);box-shadow:0 6px 24px rgba(0,0,0,.15)}
.quote h3{left:0;width:282px;top:24px;font-size:22px;font-weight:700;color:var(--ink);text-align:center}
.quote .sub{left:0;width:282px;top:54px;font-size:11px;font-style:italic;font-weight:600;color:var(--blue);text-align:center}
.field{left:28px;width:226px;height:52px;border-bottom:1px solid var(--line);font-size:11px;color:var(--muted)}
.field svg{position:absolute;left:0;top:20px}
.field span{position:absolute;left:28px;top:20px}
.quote .phone{left:28px;top:332px;font-size:12px;color:var(--ink)}
.quote .phone svg{vertical-align:middle;margin-right:6px}
.quote .btn{left:156px;top:322px;width:110px;height:34px;line-height:34px;font-size:11px}
.sec-title{left:0;width:1200px;text-align:center;font-size:28px;font-weight:700;color:var(--ink)}
.sec-sub{left:0;width:1200px;text-align:center;font-size:12px;color:var(--muted)}
.svc{top:726px;width:282px;height:393px;color:var(--white);overflow:hidden}
.svc .photo{position:absolute;inset:0}
.svc .shade{position:absolute;inset:0;background:linear-gradient(to bottom,rgba(0,0,0,0) 30%,rgba(0,0,0,.55) 100%)}
.svc h4{position:absolute;left:0;right:0;text-align:center;font-size:16px;font-weight:700;text-decoration:underline;text-underline-offset:4px}
.svc p{position:absolute;left:30px;right:30px;text-align:center;font-size:11px;line-height:17px}
.svc .more{position:absolute;left:95px;top:310px;width:92px;height:40px;line-height:38px;border:1.5px solid var(--white);border-radius:30px;text-align:center;font-size:12px;font-weight:600;background:rgba(0,0,0,.25)}
.why{left:0;top:1198px;width:1200px;height:441px;background:var(--soft)}
.why h2{left:155px;top:72px;font-size:28px;font-weight:700;color:var(--ink)}
.why-item{left:155px;width:420px;height:70px}
.why-item .ico{position:absolute;left:0;top:0;width:58px;height:58px;border-radius:50%;background:var(--white);border:2px solid var(--line)}
.why-item .ico i{position:absolute;left:12px;top:12px;width:30px;height:30px;border-radius:50%;background:#c9d6e4}
.why-item h5{position:absolute;left:76px;top:4px;font-size:15px;font-weight:700;color:var(--blue)}
.why-item p{position:absolute;left:76px;top:28px;width:310px;font-size:11px;line-height:17px}
.why .video{left:611px;top:80px;width:432px;height:280px;background:linear-gradient(160deg,#a7b3b9 0%,#7d8a73 45%,#5d5a4b 100%)}
.why .play{left:808px;top:198px}
.plan{top:1828px;height:462px;background:var(--soft);text-align:center}
.plan.featured{top:1809px;height:505px;background:var(--blue);color:var(--white);z-index:2}
.plan h5{margin-top:24px;font-size:16px;font-weight:600;color:var(--blue)}
.plan.featured h5{color:var(--white)}
.plan .tag{font-size:10px;margin-top:4px}
.plan .pin{display:block;margin:20px auto 0}
.plan ul{list-style:none;margin-top:28px;font-size:10px;line-height:16px}
.plan li{padding:6px 0;margin:0 auto;width:70%;border-bottom:1px dashed transparent}
.plan.featured li{border-bottom-color:rgba(255,255,255,.55)}
.plan .btn{margin-top:26px;width:130px;height:34px;line-height:32px;font-size:11px}
.plan.featured .btn{background:var(--white);color:var(--blue);border:none;line-height:34px}
.steps-line{left:300px;top:2527px;width:600px;height:1px;background:var(--line)}
.step{top:2478px;width:200px;text-align:center}
.step .circle{width:98px;height:98px;margin:0 auto;border-radius:50%;background:var(--white);border:2px solid var(--line);position:relative}
.step .circle i{position:absolute;left:27px;top:27px;width:40px;height:40px;border-radius:8px;background:#d6e6f2}
.step p{margin-top:22px;font-size:13px;font-weight:500;color:var(--ink)}
.testi{left:0;top:2690px;width:1200px;height:439px;background:linear-gradient(110deg,#4a3a2c 0%,#6d5a47 35%,#5a4b3d 60%,#3b3129 100%);color:var(--white)}
.testi h2{left:0;width:1200px;top:74px;text-align:center;font-size:28px;font-weight:700}
.testi .avatar{left:560px;top:125px;width:80px;height:80px;border-radius:50%;background:#c9a58d;border:3px solid var(--white)}
.testi p{left:270px;width:660px;top:236px;text-align:center;font-size:13px;line-height:23px}
.testi .name{left:0;width:1200px;top:360px;text-align:center;font-size:14px;font-weight:600;color:var(--blue)}
.testi .role{left:0;width:1200px;top:390px;text-align:center;font-size:12px}
.testi .arrow{top:213px;font-size:20px;font-weight:700}
.cta h3{left:0;width:1200px;top:3185px;text-align:center;font-size:31px;font-weight:500;color:var(--ink);line-height:38px}
.cta .btn{top:3284px;height:40px;line-height:38px;font-size:12px}
.footer{left:0;top:3367px;width:1200px;height:314px;background:var(--soft)}
.footer .logo{left:155px;top:60px;font-size:32px}
.footer .callus{left:155px;top:128px;font-size:15px;font-weight:600;color:var(--blue)}
.footer .callus b{color:var(--ink)}
.footer .mail{left:155px;top:156px;font-size:11px}
.fcol{top:60px}
.fcol h6{font-size:14px;font-weight:600;color:var(--ink);margin-bottom:14px}
.fcol a{display:block;font-size:12px;color:var(--text);text-decoration:none;margin-bottom:12px}
.fcol a.active{color:var(--blue);text-decoration:underline}
.sub-box{left:839px;top:95px;width:205px;height:36px;border:1px solid #c7ccd4;background:var(--white);font-size:11px;color:var(--muted);padding:11px 12px}
.sub-box svg{position:absolute;right:10px;top:12px}
.fsoc{left:839px;top:148px;display:flex;gap:10px}
.fsoc i{width:30px;height:30px;border-radius:50%;background:#dfe2e7;display:block}
.fsoc i.on{background:var(--blue)}
.footer .copy{left:0;width:1200px;top:248px;text-align:center;font-size:11px}
.footer .copy b{color:var(--ink)}
.totop{left:1120px;top:3606px;width:28px;height:28px;border-radius:50%;background:var(--blue)}
</style>
</head>
<body>

<div class="abs topbar">
  <div class="abs call"><b>&#9742; Call Us :</b> 123-456-7890</div>
  <div class="abs promo">Book a Local Professional <span>LumaRidge Hauling</span></div>
  <div class="abs signup">&#9679; Sign Up!</div>
  <div class="abs socials"><i></i><i></i><i></i><i></i></div>
</div>

<header class="abs nav">
  <div class="abs logo">LumaRidge</div>
  <a class="active" style="left:318px">Home</a>
  <a style="left:372px">About us</a>
  <a style="left:448px">Services</a>
  <a style="left:527px">Why Us?</a>
  <a style="left:605px">How It Works</a>
  <a style="left:707px">Pricing</a>
  <a style="left:778px">Testimonials</a>
  <a style="left:880px">Contact Us</a>
  <a class="btn btn-solid">Book a Service</a>
</header>

<section class="abs hero" role="img" aria-label="Living room doorway with stacked moving boxes and a rolled rug">
  <h1 class="abs">Book a Local<br><span>LumaRidge Hauling</span></h1>
  <a class="abs btn btn-line">Book a Service</a>
</section>

<div class="abs quote-accent"></div>
<form class="abs quote">
  <h3 class="abs">Get a Quote</h3>
  <div class="abs sub">Inquire Now!</div>
  <div class="abs field" style="top:80px"><svg width="14" height="14" viewBox="0 0 14 14"><circle cx="7" cy="4.5" r="3" fill="none" stroke="#8a909a"/><path d="M1.5 13c0-3 2.5-5 5.5-5s5.5 2 5.5 5" fill="none" stroke="#8a909a"/></svg><span>Name</span></div>
  <div class="abs field" style="top:132px"><svg width="14" height="14" viewBox="0 0 14 14"><rect x="1" y="3" width="12" height="8" fill="none" stroke="#8a909a"/><path d="M1 3l6 5 6-5" fill="none" stroke="#8a909a"/></svg><span>Email</span></div>
  <div class="abs field" style="top:184px"><svg width="14" height="14" viewBox="0 0 14 14"><path d="M3 1l2.5 3-1.5 1.5c1 2 2.5 3.5 4.5 4.5L10 8.5l3 2.5-1.5 2C6 12.5 1.5 8 1 2.5z" fill="none" stroke="#8a909a"/></svg><span>Phone</span></div>
  <div class="abs field" style="top:236px;height:60px"><svg width="14" height="14" viewBox="0 0 14 14"><path d="M2 12l1-3 7-7 2 2-7 7z" fill="none" stroke="#8a909a"/></svg><span>Type Your Message</span></div>
  <div class="abs phone"><svg width="18" height="18" viewBox="0 0 18 18"><circle cx="9" cy="9" r="8" fill="none" stroke="#1b1b1b"/><path d="M6 5l1.5 2-1 1c.6 1.3 1.6 2.3 2.8 2.8l1-1 2 1.5-1 1.3C8.5 12.3 5.7 9.5 5 6z" fill="#1b1b1b"/></svg>123-456-7890</div>
  <a class="abs btn btn-solid">Get a Quote</a>
</form>

<h2 class="abs sec-title" style="top:640px">What We Do?</h2>
<p class="abs sec-sub" style="top:682px">Contrary to popular belief, Lorem Ipsum is not simply random text.</p>

<div class="abs svc" style="left:155px">
  <div class="photo" role="img" aria-label="Stacked cardboard boxes marked fragile" style="background:linear-gradient(160deg,#8a6f55,#5b4634 60%,#3a2c22)"></div>
  <div class="shade"></div>
  <h4 style="top:185px">Packers</h4>
  <p style="top:222px">Lorem ipsum dolor sit amet, consectetur adipiscing elit, sed do eiusmod tempor ...</p>
  <div class="more">More</div>
</div>
<div class="abs svc" style="left:459px">
  <div class="photo" role="img" aria-label="Installer assembling furniture on the floor" style="background:linear-gradient(160deg,#7f9a8a,#4f6f7d 55%,#2c3a44)"></div>
  <div class="shade"></div>
  <h4 style="top:265px">Installer</h4>
  <p style="top:298px">Lorem ipsum dolor sit amet, consectetur adipiscing elit, sed do eiusmod tempor ...</p>
</div>
<div class="abs svc" style="left:763px">
  <div class="photo" role="img" aria-label="Crew unloading boxes from a rental truck" style="background:linear-gradient(160deg,#6b5d50,#8a6b4f 50%,#3b3028)"></div>
  <div class="shade"></div>
  <h4 style="top:265px">Rental Trucks Assistant</h4>
  <p style="top:298px">Lorem ipsum dolor sit amet, consectetur adipiscing elit, sed do eiusmod tempor ...</p>
</div>

<section class="abs why">
  <h2 class="abs">Why Us?</h2>
  <div class="abs why-item" style="top:130px"><div class="ico"><i></i></div><h5>Trusted Professionals</h5><p>There are many variations of passages of Lorem Ipsum available, but the majority</p></div>
  <div class="abs why-item" style="top:213px"><div class="ico"><i></i></div><h5>Same Day Availability</h5><p>There are many variations of passages of Lorem Ipsum available, but the majority</p></div>
  <div class="abs why-item" style="top:294px"><div class="ico"><i></i></div><h5>Our Guarantee</h5><p>There are many variations of passages of Lorem Ipsum available, but the majority</p></div>
  <div class="abs video" role="img" aria-label="Movers carrying boxes from a house to the street"></div>
  <svg class="abs play" width="38" height="38" viewBox="0 0 38 38"><circle cx="19" cy="19" r="19" fill="#fff"/><path d="M15 12l11 7-11 7z" fill="#1b1b1b"/></svg>
</section>

<h2 class="abs sec-title" style="top:1710px">Perfect Pricing</h2>
<p class="abs sec-sub" style="top:1754px">Contrary to popular belief, Lorem Ipsum is not simply random text.</p>

<div class="abs plan" style="left:81px;width:238px">
  <h5>Basic Plan</h5><div class="tag">There are many variations</div>
  <svg class="pin" width="110" height="130" viewBox="0 0 110 130"><path d="M55 128L18 92A52 52 0 1 1 92 92z" fill="#0a8fd0"/><text x="55" y="63" text-anchor="middle" fill="#fff" font-family="Montserrat,sans-serif" font-size="30" font-weight="500"><tspan font-size="14" dy="-10">$</tspan><tspan dy="10">99</tspan></text><text x="55" y="80" text-anchor="middle" fill="#fff" font-family="Montserrat,sans-serif" font-size="10">pm</text></svg>
  <ul><li>Get all the premium</li><li>Features in our popular Pro</li><li>Plan, plus unlimited users,</li><li>priority support and</li></ul>
  <a class="btn btn-line">Book Now!</a>
</div>
<div class="abs plan featured" style="left:319px;width:295px">
  <h5 style="margin-top:44px">Moving</h5><div class="tag">There are many variations text</div>
  <svg class="pin" width="110" height="130" viewBox="0 0 110 130"><path d="M55 128L18 92A52 52 0 1 1 92 92z" fill="#fff"/><text x="55" y="63" text-anchor="middle" fill="#0a8fd0" font-family="Montserrat,sans-serif" font-size="30" font-weight="500"><tspan font-size="14" dy="-10">$</tspan><tspan dy="10">199</tspan></text><text x="55" y="80" text-anchor="middle" fill="#0a8fd0" font-family="Montserrat,sans-serif" font-size="10">pm</text></svg>
  <ul><li>Get all the premium</li><li>Features in our popular Pro</li><li>Plan, plus unlimited users,</li><li>priority support and</li></ul>
  <a class="btn btn-line">Book Now!</a>
</div>
<div class="abs plan" style="left:614px;width:240px">
  <h5>Packing</h5><div class="tag">There are many variations</div>
  <svg class="pin" width="110" height="130" viewBox="0 0 110 130"><path d="M55 128L18 92A52 52 0 1 1 92 92z" fill="#0a8fd0"/><text x="55" y="63" text-anchor="middle" fill="#fff" font-family="Montserrat,sans-serif" font-size="30" font-weight="500"><tspan font-size="14" dy="-10">$</tspan><tspan dy="10">80</tspan></text><text x="55" y="80" text-anchor="middle" fill="#fff" font-family="Montserrat,sans-serif" font-size="10">pm</text></svg>
  <ul><li>Get all the premium</li><li>Features in our popular Pro</li><li>Plan, plus unlimited users,</li><li>priority support and</li></ul>
  <a class="btn btn-line">Book Now!</a>
</div>
<div class="abs plan" style="left:878px;width:241px">
  <h5>Installation</h5><div class="tag">There are many variations</div>
  <svg class="pin" width="110" height="130" viewBox="0 0 110 130"><path d="M55 128L18 92A52 52 0 1 1 92 92z" fill="#0a8fd0"/><text x="55" y="63" text-anchor="middle" fill="#fff" font-family="Montserrat,sans-serif" font-size="30" font-weight="500"><tspan font-size="14" dy="-10">$</tspan><tspan dy="10">100</tspan></text><text x="55" y="80" text-anchor="middle" fill="#fff" font-family="Montserrat,sans-serif" font-size="10">pm</text></svg>
  <ul><li>Get all the premium</li><li>Features in our popular Pro</li><li>Plan, plus unlimited users,</li><li>priority support and</li></ul>
  <a class="btn btn-line">Book Now!</a>
</div>

<h2 class="abs sec-title" style="top:2387px">How It Works?</h2>
<p class="abs sec-sub" style="top:2431px">Contrary to popular belief, Lorem Ipsum is not simply random text.</p>
<div class="abs steps-line"></div>
<div class="abs step" style="left:158px"><div class="circle"><i role="img" aria-label="Service checklist icon"></i></div><p>Select Your Service</p></div>
<div class="abs step" style="left:386px"><div class="circle"><i role="img" aria-label="Calendar icon"></i></div><p>Select Your Time &amp; Date</p></div>
<div class="abs step" style="left:614px"><div class="circle"><i role="img" aria-label="Secure payment icon"></i></div><p>Pay Securely Online</p></div>
<div class="abs step" style="left:840px"><div class="circle"><i role="img" aria-label="Relaxed customer icon"></i></div><p>Sit Back, Relax and Wait</p></div>

<section class="abs testi" role="img" aria-label="Blurred background of a couple packing boxes at home">
  <h2 class="abs">Testimonials</h2>
  <div class="abs avatar" role="img" aria-label="Customer portrait"></div>
  <p class="abs">But I must explain to you how all this mistaken idea of denouncing pleasure and praising work pain was born and I will give you a complete account of the system, and expound the actual teachings of the great explorer of the truth, the master-builder circumstances occur in which toil and pain can procure him some great pleasure ...</p>
  <div class="abs name">- Standard Chunk -</div>
  <div class="abs role">House Wife</div>
  <div class="abs arrow" style="left:155px">&#8249;</div>
  <div class="abs arrow" style="left:1036px">&#8250;</div>
</section>

<section class="cta">
  <h3 class="abs">Contrary to popular belief,<br>There are many variations of passages.</h3>
  <a class="abs btn btn-solid" style="left:373px;width:220px">Book Your Services</a>
  <a class="abs btn btn-line" style="left:608px;width:220px">Explore Our Pricing plan</a>
</section>

<footer class="abs footer">
  <div class="abs logo">LumaRidge</div>
  <div class="abs callus">Call Us : <b>&#9742; 123-456-7890</b></div>
  <div class="abs mail">info@lumaridgehauling.example</div>
  <div class="abs fcol" style="left:407px"><h6>Browse Website</h6><a class="active">About Us</a><a>Pricing</a><a>Testimonials</a><a>Contact Us</a></div>
  <div class="abs fcol" style="left:611px"><h6>Our Services</h6><a>Packers</a><a>Installer</a><a>Rental Trucks Assistant</a></div>
  <div class="abs fcol" style="left:839px"><h6>Subscribe Us</h6></div>
  <div class="abs sub-box">Your email ...<svg width="14" height="10" viewBox="0 0 14 10"><path d="M0 5h12M8 1l4 4-4 4" fill="none" stroke="#555b66"/></svg></div>
  <div class="abs fsoc"><i></i><i class="on"></i><i></i><i></i></div>
  <div class="abs copy">© 2016 <b>LumaRidge</b>. All Right Reserved.</div>
</footer>
<svg class="abs totop" viewBox="0 0 28 28"><circle cx="14" cy="14" r="14" fill="#0a8fd0"/><path d="M9 16l5-5 5 5" fill="none" stroke="#fff" stroke-width="2"/></svg>

</body>
</html>
```